Healthcare IT company looking for business card design

We develop IT systems for healthcare that significantly reduces cost and improves quality.

We want a business card design that is professional and clean, and using the colors in our logo.

Doctors and decision makers in the healthcare industry

Healthcare

It should include
Name and title, address, telephone

Torvald Eskberg, CEO
+46 712 480517
torvald@velpamo.se

Serif

0355a3
ed282f

• Clean design
• Professional feel
• N/A
• N/A

```html
<!DOCTYPE html>
<html lang="en">
<head>
<meta charset="utf-8">
<title>Velpamo – Business Card</title>
<link href="https://fonts.googleapis.com/css2?family=Source+Sans+3:wght@400;700&display=swap" rel="stylesheet">
<style>
  :root {
    --brand-blue: #0355a3;
    --card-light: #f5f2f1;
    --stage: #e6e7ea;
    --ink-light: #ffffff;
  }
  html, body {
    margin: 0;
    width: 1200px;
    height: 900px;
    overflow: hidden;
    background: var(--stage);
    font-family: "Source Sans 3", "Myriad Pro", Arial, sans-serif;
  }
  .canvas {
    position: relative;
    width: 1200px;
    height: 900px;
  }
  .business-card {
    position: absolute;
    left: 301px;
    top: 213px;
    width: 617px;
    height: 383px;
    display: flex;
    box-shadow: 0 10px 30px rgba(0, 0, 0, 0.12);
  }
  .brand-side {
    width: 308px;
    height: 100%;
    background: var(--card-light);
    display: flex;
    align-items: center;
    justify-content: center;
  }
  .brand-name {
    margin-top: -6px;
    font-size: 56px;
    font-weight: 400;
    color: var(--brand-blue);
    line-height: 1;
  }
  .contact-side {
    width: 309px;
    height: 100%;
    background: var(--brand-blue);
    color: var(--ink-light);
    box-sizing: border-box;
    padding: 104px 20px 0 36px;
  }
  .person-name {
    margin: 0;
    font-size: 21px;
    font-weight: 700;
    line-height: 26px;
  }
  .person-title {
    margin: 0;
    font-size: 17px;
    font-weight: 400;
    line-height: 22px;
  }
  .address {
    margin: 14px 0 0;
    font-size: 17px;
    line-height: 22px;
    font-style: normal;
  }
  .contact-list {
    list-style: none;
    margin: 18px 0 0;
    padding: 0;
    font-size: 17px;
    line-height: 22px;
  }
  .contact-item {
    display: flex;
    align-items: center;
    gap: 13px;
  }
  .contact-icon {
    width: 13px;
    height: 13px;
    fill: var(--ink-light);
    flex: none;
  }
</style>
</head>
<body>
<div class="canvas">
  <div class="business-card">
    <div class="brand-side">
      <span class="brand-name">Velpamo</span>
    </div>
    <div class="contact-side">
      <h1 class="person-name">Torvald Eskberg</h1>
      <p class="person-title">CEO</p>
      <address class="address">12345, Address Goes Here<br>Country Name, 123456.</address>
      <ul class="contact-list">
        <li class="contact-item">
          <svg class="contact-icon" viewBox="0 0 24 24" aria-hidden="true"><path d="M6.6 10.8a15.1 15.1 0 0 0 6.6 6.6l2.2-2.2a1 1 0 0 1 1-.25 11.4 11.4 0 0 0 3.6.57 1 1 0 0 1 1 1V20a1 1 0 0 1-1 1A17 17 0 0 1 3 4a1 1 0 0 1 1-1h3.5a1 1 0 0 1 1 1c0 1.25.2 2.45.57 3.57a1 1 0 0 1-.25 1z"/></svg>
          <span>+46 712 480517</span>
        </li>
        <li class="contact-item">
          <svg class="contact-icon" viewBox="0 0 24 24" aria-hidden="true"><path d="M2 6.5V19h20V6.5l-10 7.5z M2.5 5h19L12 12z"/></svg>
          <span>torvald@velpamo.se</span>
        </li>
      </ul>
    </div>
  </div>
</div>
</body>
</html>
```